Commercial Loan Originator Business Card (CHANGE COLORS SCHEME)

CHANGE COLOR SCHEME - SAME DESIGN

Name Marissa Lantham
Title Commercial Loan Originator
Office (800) 641-2905 x68
Direct (240) 617-2435
Email brightleaf4you@mailpost.example

Name Derek Fallow
Office (800) 641-2905 x70
Direct (410) 932-1864
Email d.falthebroker@mailpost.example

Name Gordon Wexley
Office (800) 641-2905 x71
Direct (215) 346-2081
Email g.wexley37@mailpost.example

Name Lyn Moreau
Office (800) 641-2905 x
Direct (202) 458-1937
Email lmoreau64@mailpost.example

Name Nadia Strand
Office (800) 641-2905 x72
Direct (240) 871-5246
Email qrzhomelending@mailpost.example

```html
<!DOCTYPE html>
<html lang="en">
<head>
<meta charset="utf-8">
<title>Derek Fallow – Commercial Loan Originator</title>
<link rel="stylesheet" href="https://fonts.googleapis.com/css2?family=Crimson+Text:wght@600&family=Poppins:wght@400&display=swap">
<style>
  :root {
    --bg: #e9e9ea;
    --card: #ffffff;
    --accent: #0e7c86;
    --ink: #1f1f22;
    --dark-wave: #1c2b45;
    --photo-top: #6d7268;
    --photo-bottom: #3c4038;
  }
  html, body {
    margin: 0;
    width: 1200px;
    height: 952px;
    overflow: hidden;
    background: var(--bg);
  }
  .business-card {
    position: absolute;
    left: 40px;
    top: 129px;
    width: 1120px;
    height: 694px;
    background: var(--card);
    border-radius: 48px;
    overflow: hidden;
  }
  .card-art {
    position: absolute;
    inset: 0;
    width: 100%;
    height: 100%;
  }
  .name-marker {
    position: absolute;
    left: 0;
    top: 97px;
    width: 28px;
    height: 68px;
    background: var(--accent);
  }
  .person-name {
    position: absolute;
    left: 47px;
    top: 84px;
    margin: 0;
    font-family: "Crimson Text", Georgia, serif;
    font-weight: 600;
    font-size: 54px;
    line-height: 1;
    letter-spacing: 0.5px;
    text-transform: uppercase;
    color: var(--accent);
  }
  .person-title {
    position: absolute;
    left: 49px;
    top: 138px;
    margin: 0;
    font-family: "Poppins", Arial, sans-serif;
    font-size: 32px;
    line-height: 1.2;
    color: var(--ink);
  }
  .contact-list {
    position: absolute;
    left: 52px;
    top: 315px;
    margin: 0;
    padding: 0;
    list-style: none;
    font-family: "Poppins", Arial, sans-serif;
    font-size: 32px;
    color: var(--ink);
  }
  .contact-item {
    display: flex;
    align-items: center;
    height: 41px;
    white-space: nowrap;
  }
  .contact-icon {
    width: 32px;
    height: 32px;
    margin-right: 16px;
    flex: none;
  }
  .contact-item.email .contact-icon { margin-right: 22px; }
  .contact-label { color: var(--accent); margin-left: 12px; }
</style>
</head>
<body>
  <div class="business-card">
    <svg class="card-art" viewBox="0 0 1058 655" preserveAspectRatio="none">
      <defs>
        <linearGradient id="portraitTone" x1="0" y1="0" x2="0" y2="1">
          <stop offset="0" stop-color="var(--photo-top)"/>
          <stop offset="1" stop-color="var(--photo-bottom)"/>
        </linearGradient>
      </defs>
      <rect role="img" aria-label="Portrait photo of the loan originator in a dark green suit" x="705" y="87" width="330" height="520" rx="30" fill="url(#portraitTone)"/>
      <path d="M0 497 C 90 465 170 455 255 460 C 420 470 560 540 660 575 L 0 575 Z" fill="var(--dark-wave)"/>
      <path d="M0 541 C 90 508 170 490 255 492 C 420 498 560 560 720 590 C 860 617 960 606 1058 578 L 1058 655 L 0 655 Z" fill="#fff"/>
      <path d="M0 550 C 90 517 170 499 255 501 C 420 507 560 568 720 598 C 860 624 960 614 1058 586 L 1058 655 L 0 655 Z" fill="var(--accent)"/>
    </svg>

    <div class="name-marker"></div>
    <h1 class="person-name">Derek Fallow</h1>
    <p class="person-title">Commercial Loan Originator</p>

    <ul class="contact-list">
      <li class="contact-item">
        <svg class="contact-icon" viewBox="0 0 24 24" aria-hidden="true"><path d="M6.6 2.5 9.2 6.3 7.6 8.3c.9 2.6 3.4 5.2 6.1 6.1l2-1.6 3.8 2.6-1.4 3.4c-.4.9-1.4 1.3-2.3 1-6.2-1.9-10.1-5.8-12-12-.3-.9.1-1.9 1-2.3Z" fill="none" stroke="var(--accent)" stroke-width="2" stroke-linejoin="round"/><path d="M14 3.5a7 7 0 0 1 6.5 6.5M14 7a3.5 3.5 0 0 1 3 3" fill="none" stroke="var(--accent)" stroke-width="2" stroke-linecap="round"/></svg>
        <span>(800) 641-2905 x70</span>
      </li>
      <li class="contact-item">
        <svg class="contact-icon" viewBox="0 0 24 24" aria-hidden="true"><path d="M6.6 2.5 9.2 6.3 7.6 8.3c.9 2.6 3.4 5.2 6.1 6.1l2-1.6 3.8 2.6-1.4 3.4c-.4.9-1.4 1.3-2.3 1-6.2-1.9-10.1-5.8-12-12-.3-.9.1-1.9 1-2.3Z" fill="none" stroke="var(--accent)" stroke-width="2" stroke-linejoin="round"/><path d="M14 3.5a7 7 0 0 1 6.5 6.5M14 7a3.5 3.5 0 0 1 3 3" fill="none" stroke="var(--accent)" stroke-width="2" stroke-linecap="round"/></svg>
        <span>(410) 932-1864<span class="contact-label">(Direct )</span></span>
      </li>
      <li class="contact-item email">
        <svg class="contact-icon" viewBox="0 0 24 24" aria-hidden="true"><rect x="1" y="5" width="22" height="15" fill="var(--accent)"/><path d="M1 5 12 14 23 5M1 20 9 12M23 20 15 12" fill="none" stroke="#fff" stroke-width="1.5"/></svg>
        <span>d.falthebroker@mailpost.example</span>
      </li>
    </ul>
  </div>
</body>
</html>
```